Need new clean look for TorvenPlex.com Homepage

Looking for a complete redesign of our homepage that will be built on Bootstrap 4. Our current page exists at www.torvenplex.com
The layout is fairly simple with a new header, footer, and two column layout. The header features a top slim nav with event names, our logo, main navigation and a fighter search field. The right column features several content widgets and the left column (or main content area) features two columns of dynamically sized content boxes. Those boxes will feature seven different types of content and the containing box should be designed to clearly indicate the type of content (Editorial Blog, External Link, Embedded Video, Quick News Text, KW Post, Lumavoxa Post, Zumblo Post). These content boxes will also be numbered sequentially.
Mixed Martial Arts, Sports
1 page

```html
<!DOCTYPE html>
<html lang="en">
<head>
<meta charset="utf-8">
<title>TorvenPlex.com — Home</title>
<link href="https://fonts.googleapis.com/css2?family=Roboto:wght@400;500;700&family=Amatic+SC:wght@400;700&display=swap" rel="stylesheet">
<style>
:root{
  --red:#c8102e;
  --bar:#dedede;
  --card-head:#cccccc;
  --line:#c9c9c9;
  --text:#555;
  --green:#2fa84a;
  --panel:#e2e2e2;
}
*{box-sizing:border-box;margin:0;padding:0}
html,body{width:741px;height:1200px;overflow:hidden;background:#fff;font-family:"Roboto",Arial,sans-serif;color:var(--text)}
.page{position:relative;width:741px;height:1200px}
.abs{position:absolute}
.site-header{position:absolute;left:0;top:0;width:741px;height:64px;background:var(--bar)}
.event-strip{position:absolute;top:12px;left:60px;display:flex;gap:26px;font-size:7px;color:#666}
.brand{position:absolute;left:61px;top:36px;font-size:14px;font-weight:700;color:#fff;letter-spacing:.5px;display:flex;align-items:center;gap:5px}
.brand-mark{width:11px;height:11px;background:var(--red)}
.main-nav{position:absolute;left:302px;top:34px;display:flex;gap:6px}
.main-nav a{display:block;background:var(--red);color:#fff;font-size:7.5px;font-weight:500;padding:0 9px;height:20px;line-height:20px;border-radius:3px;text-decoration:none}
.fighter-search{position:absolute;left:595px;top:34px;width:85px;height:20px;border:1px solid #bbb;border-radius:10px;background:#e9e9e9;font-size:7px;color:#888;padding-left:9px;line-height:18px}
.fighter-search i{position:absolute;right:2px;top:2px;width:14px;height:14px;border-radius:50%;background:#aaa}
.hero{position:absolute;left:0;top:64px;width:741px;height:132px;background:linear-gradient(90deg,#1ff018,#2cf523 60%,#28ee20)}
.trending{position:absolute;left:61px;top:210px;width:437px;height:35px;background:var(--red);border-radius:4px;color:#fff;font-size:10px;font-weight:700;text-align:center;line-height:35px;letter-spacing:.2px}
.card{position:absolute;background:#fff;border:1px solid var(--line)}
.card-head{height:30px;background:var(--card-head);display:flex;align-items:center;padding:0 7px;gap:8px;font-size:7px;font-weight:500;color:#555}
.card-num{width:18px;height:18px;border-radius:50%;background:#fff;border:1px solid #bbb;font-size:7.5px;color:#333;text-align:center;line-height:16px;flex:none}
.card-title{flex:1;white-space:nowrap;overflow:hidden}
.type-icon{flex:none;width:15px;height:13px}
.type-dot{flex:none;width:15px;height:15px;border-radius:50%}
.media{width:100%}
.copy{font-size:6.8px;line-height:12.5px;color:#777;padding:6px 10px}
.read-more{font-size:7.2px;color:var(--red);font-weight:500;text-align:right;padding-right:15px}
.scroll-box{position:relative;margin:8px;height:70px;font-size:6.8px;line-height:15px;color:#777;padding-right:20px}
.scroll-box::after{content:"";position:absolute;right:0;top:4px;width:9px;height:62px;border:1px solid #bbb;border-radius:4px;background:#f4f4f4}
.side{position:absolute;left:521px;width:158px}
.side-head{height:28px;background:var(--red);border-radius:4px 4px 0 0;color:#fff;font-size:7.5px;font-weight:500;text-align:center;line-height:28px}
.ad{border:1px solid var(--line);background:#fff}
.ad-title{font-family:"Amatic SC",cursive;color:#444;text-align:center}
.headlines{background:var(--panel);padding:8px 10px 6px 10px}
.headlines li{list-style:none;position:relative;padding-left:16px;font-size:6.8px;line-height:16px;color:#777}
.headlines li::before{content:"";position:absolute;left:1px;top:5px;width:6px;height:6px;border-radius:50%;background:#777}
.stat{position:absolute;width:66px;height:19px;font-size:7px;line-height:19px;padding-left:10px;border:1px solid #ccc;color:#777}
.stat.win{background:var(--green);border-color:var(--green);color:#fff;font-weight:500}
.site-footer{position:absolute;left:61px;top:1120px;width:618px;height:80px;background:#e3e3e3}
.footer-links{position:absolute;left:17px;top:14px;display:flex;gap:22px;font-size:7.2px;color:#555}
.footer-links .sep{color:#777}
.footer-info{position:absolute;left:17px;top:30px;font-size:7.2px;line-height:18px;color:#666}
.footer-apps{position:absolute;right:20px;top:30px;display:flex;gap:10px;font-size:7.5px;font-weight:700;color:#333;align-items:center}
.play{position:absolute;width:28px;height:28px;border-radius:50%;border:2px solid #fff;left:50%;top:50%;transform:translate(-50%,-50%)}
.play::after{content:"";position:absolute;left:10px;top:7px;border-left:9px solid #fff;border-top:5px solid transparent;border-bottom:5px solid transparent}
</style>
</head>
<body>
<div class="page">

<header class="site-header">
  <nav class="event-strip">
    <span>Sat 2/8- CFL 124 (Los Angeles, CA)</span>
    <span>Ft. 2/16 Ironhall 124 (St. Louis, MO)</span>
    <span>Sat 2/17 CFL Fight Night 126 (Belem, Brazil)</span>
    <span>Sat 4/7- CFL 223 (Brooklyn, NY)</span>
  </nav>
  <div class="brand"><span class="brand-mark"></span>THE VAULT</div>
  <nav class="main-nav">
    <a href="#">NEWS</a><a href="#">FORUMS</a><a href="#">EVENTS</a><a href="#">FIGHTERS</a><a href="#">ACCOUNT</a>
  </nav>
  <div class="fighter-search">Fighter search<i></i></div>
</header>

<div class="hero" role="img" aria-label="Bold graphic banner with a snarling cartoon fight character on a bright green background"></div>

<div class="trending">TRENDING CONTENT</div>

<article class="card" style="left:62px;top:260px;width:209px;height:216px">
  <div class="card-head"><span class="card-num">1</span><span class="card-title">Darrow self-imposes concussion protocol</span>
    <svg class="type-icon" viewBox="0 0 15 13"><rect x="1" y="2" width="12" height="10" fill="none" stroke="#777"/><path d="M3 5h8M3 7h8M3 9h6" stroke="#777"/></svg></div>
  <div class="media" style="height:122px;background:linear-gradient(120deg,#6b4a38,#2d2a28 60%,#8b8b8b)" role="img" aria-label="Fighter taking a selfie beside the cage"></div>
  <p class="copy">Sed ut perspiciatis unde omnis iste natus error voluptatem accusantium doloremque laudantium, totam rem aperiam, eaque ipsa quae ab illum qui dolorem</p>
  <div class="read-more">Read More &rarr;</div>
</article>

<article class="card" style="left:62px;top:494px;width:209px;height:214px">
  <div class="card-head"><span class="card-num">3</span><span class="card-title">Okonji wins main event</span><span class="type-dot" style="background:#1da1f2"></span></div>
  <div style="display:flex;gap:5px;padding:6px 8px 0;font-size:4.5px;color:#333;line-height:6px"><span style="width:12px;height:12px;border-radius:50%;background:#555;flex:none"></span><span><b>CFL</b> @cfl · 38m<br>Homecoming complete.</span></div>
  <p style="font-size:6.4px;color:#555;padding:3px 0 0 26px">Dolorem ipsum quia dolor amet, <span style="color:var(--red)">consectetur.shrt.vx236</span></p>
  <div class="abs" style="left:26px;top:70px;width:173px;height:120px;background:linear-gradient(160deg,#3a3030,#6a5548 50%,#2a2a2a)" role="img" aria-label="Winner standing over opponent in the cage"></div>
  <div class="abs" style="left:28px;top:196px;font-size:7px;color:#555;display:flex;gap:12px"><span>&#9993; 9</span><span>&#8635; 6</span><span>&#9829; 5</span><span>&#9993; 7</span></div>
</article>

<article class="card" style="left:62px;top:726px;width:209px;height:184px">
  <div class="card-head"><span class="card-num">6</span><span class="card-title">Brandt: Castell's legacy is definitely tarnished</span>
    <svg class="type-icon" viewBox="0 0 15 13"><rect x="2" y="3" width="8" height="8" fill="none" stroke="#777"/><path d="M7 2h5v5M12 2L6 8" fill="none" stroke="#777"/></svg></div>
  <div class="media" style="height:124px;background:linear-gradient(150deg,#2a2a2c,#5a4a40 55%,#1e1e20)" role="img" aria-label="Fighter celebrating with arm raised in the octagon"></div>
  <p style="font-size:7.5px;color:#333;padding:9px 10px">Source: quis nostrum exercitationem</p>
</article>

<article class="card" style="left:62px;top:925px;width:209px;height:117px">
  <div class="card-head"><span class="card-num">8</span><span class="card-title">CFL Fight Night 126 weigh-in alert</span><span class="type-dot" style="background:#777"></span></div>
  <div class="scroll-box">Sed ut perspiciatis unde omnis iste natus error sit voluptatem accusantium doloremque laudantium, totam rem aperiam, eaque ipsa quae ab illo inventore</div>
</article>

<article class="card" style="left:288px;top:260px;width:210px;height:117px">
  <div class="card-head"><span class="card-num">2</span><span class="card-title">Kessing Injured, out of CFL 222</span><span class="type-dot" style="background:#777"></span></div>
  <div class="scroll-box">Sed ut perspiciatis unde omnis iste natus error sit voluptatem accusantium doloremque laudantium, totam rem aperiam, eaque ipsa quae ab illo inventore</div>
</article>

<article class="card" style="left:288px;top:394px;width:210px;height:152px">
  <div class="card-head"><span class="card-num">4</span><span class="card-title">Free Fight: Brandt vs. Varela</span>
    <svg class="type-icon" viewBox="0 0 15 13"><rect x="1" y="2" width="13" height="9" fill="#777"/><path d="M3 4h9M3 9h9" stroke="#ccc"/></svg></div>
  <div class="media" style="position:relative;height:122px;background:linear-gradient(90deg,#1e1e1e,#3a3532 45%,#151515)" role="img" aria-label="Embedded fight video with two fighters facing off">
    <span class="play"></span>
    <div class="abs" style="left:10px;right:10px;bottom:10px;height:2px;background:#666"><span style="display:block;width:20%;height:2px;background:var(--red)"></span></div>
  </div>
</article>

<article class="card" style="left:288px;top:563px;width:210px;height:289px">
  <div class="card-head"><span class="card-num">5</span><span class="card-title">Mireles blasts Varela</span><span class="type-dot" style="background:#e1306c;border-radius:3px"></span></div>
  <div class="media" style="height:122px;background:linear-gradient(90deg,#2a2a2a,#7a6a60 30%,#3a2a2a 70%,#1f1f1f)" role="img" aria-label="Two fighters posing with a championship belt"></div>
  <div style="display:flex;align-items:center;gap:6px;padding:12px 12px 0;font-size:7px;color:#333"><span style="width:20px;height:20px;border-radius:50%;background:#999"></span>By Someone <span style="width:4px;height:4px;border-radius:50%;background:#1a73e8"></span> Following</div>
  <p class="copy" style="padding:6px 13px 2px;line-height:12px">Sed ut perspiciatis unde omnis iste natus error sit voluptatem accusantium doloremque laudantium, totam rem aperiam,</p>
  <p style="font-size:7.2px;color:#555;padding:3px 13px">Load More Comments...</p>
  <p style="font-size:7.2px;color:#333;padding:3px 13px">&#9829; 20 Likes</p>
  <div style="margin:5px 18px 0 13px;height:18px;border:1px solid #ccc;font-size:6.8px;color:#888;padding-left:7px;line-height:16px">Add a comment</div>
</article>

<article class="card" style="left:288px;top:870px;width:210px;height:215px">
  <div class="card-head"><span class="card-num">7</span><span class="card-title">Quick Fox: Why I am the P4P best</span>
    <svg class="type-icon" viewBox="0 0 15 13"><rect x="1" y="2" width="12" height="10" fill="none" stroke="#777"/><path d="M3 5h8M3 7h8M3 9h6" stroke="#777"/></svg></div>
  <div class="media" style="height:121px;background:linear-gradient(160deg,#2b2b2b,#4a4040 50%,#1b1b1b)" role="img" aria-label="Referee raising the winner's hand after a bout"></div>
  <p class="copy">Sed ut perspiciatis unde omnis iste natus error voluptatem accusantium doloremque laudantium, totam rem aperiam, eaque ipsa quae ab illum qui dolorem</p>
  <div class="read-more">Read More &rarr;</div>
</article>

<aside class="side ad" style="top:210px;height:132px">
  <div style="height:90px;background:linear-gradient(135deg,#fbe3e8,#f7d3dc)" role="img" aria-label="Gold heart earrings on a pink background">
    <p class="ad-title" style="font-size:17px;line-height:18px;padding-top:4px">This Valentine's Be<br>Spoilt for Choice!</p>
  </div>
  <div style="display:flex;align-items:center;justify-content:center;gap:5px;height:40px;font-size:11px;color:#1b3f8a;font-weight:500"><span style="width:8px;height:8px;background:#1b3f8a"></span>Garnetlane</div>
</aside>

<aside class="side" style="top:358px">
  <div class="side-head">LATEST HEADLINES</div>
  <ul class="headlines" style="border-radius:0 0 4px 4px;height:108px">
    <li>Eu fugiat nulla pariatur. Excepteur sint occaecat cupidatat proident,</li>
    <li>Sunt in culpa qui officia deserunt mollit anim id est laborum</li>
    <li>Ullamco laboris nisi ut aliquip ex ea commodo consequat</li>
  </ul>
</aside>

<aside class="side" style="top:511px;height:245px">
  <div class="side-head">FEATURED EVENT</div>
  <p style="background:var(--panel);font-size:6.6px;color:#777;text-align:center;line-height:10px;padding:7px 6px 3px;height:31px">Lorem ipsum dolor sit amet, consectetur adipiscing eli sed do eiusmod</p>
  <div style="height:84px;background:linear-gradient(90deg,#5a3e30,#c0324a 45%,#3a5aa0 60%,#6a5a50)" role="img" aria-label="Two headline fighters in front of their national flags"></div>
  <div class="abs" style="left:0;top:143px;width:66px;height:19px;background:#ccc;font-size:7px;font-weight:500;color:#555;text-align:center;line-height:19px">MAGNAM</div>
  <div class="abs" style="left:92px;top:143px;width:66px;height:19px;background:#ccc;font-size:7px;font-weight:500;color:#555;text-align:center;line-height:19px">VOLUPTATEM</div>
  <div class="stat win" style="left:0;top:171px">Record: 19-2</div>
  <div class="stat" style="left:92px;top:171px">Record: 15-4</div>
  <div class="stat" style="left:0;top:197px">Win Streak: 2</div>
  <div class="stat win" style="left:92px;top:197px">Win Streak: 4</div>
  <div class="stat win" style="left:0;top:223px">Rank: 1</div>
  <div class="stat" style="left:92px;top:223px">Rank: 2</div>
</aside>

<aside class="side ad" style="top:771px;height:153px">
  <div style="height:20px;background:#ccc;font-size:7px;font-weight:500;color:#555;text-align:center;line-height:20px">Bout Result : TBD</div>
  <div style="height:132px;background:linear-gradient(160deg,#fdf0ee,#f3d4d4 60%,#e9c0c4)" role="img" aria-label="Silver rose ring among soft pink roses">
    <p class="ad-title" style="font-size:22px;line-height:24px;text-align:left;padding:2px 10px">This Valentine's<br>Choose Roses that<br>won't wither</p>
  </div>
</aside>

<aside class="side" style="top:945px">
  <div class="side-head">REMIX</div>
  <div style="position:relative;height:92px;background:linear-gradient(140deg,#3a5a9a,#d8dde8 45%,#5a6a8a)" role="img" aria-label="Grappling match video in white gis"><span class="play"></span></div>
  <div style="display:flex;justify-content:space-between;margin-top:9px">
    <div style="width:47px;height:34px;background:linear-gradient(135deg,#3a3a3a,#8a6a5a)" role="img" aria-label="Fighter interview still"></div>
    <div style="width:47px;height:34px;background:linear-gradient(135deg,#a88a7a,#e0c8b8)" role="img" aria-label="Coach portrait still"></div>
    <div style="width:47px;height:34px;background:linear-gradient(135deg,#1a1a1a,#5a5040)" role="img" aria-label="Fight highlight video still"></div>
  </div>
</aside>

<footer class="site-footer">
  <nav class="footer-links"><span>ABOUT</span><span class="sep">|</span><span>ADVERTISING</span><span class="sep">|</span><span>CREATE ACCOUNT</span><span class="sep">|</span><span>LINKS</span><span class="sep">|</span><span>CONTACT US</span></nav>
  <div class="footer-info">TorvenPlex LLC. 88 Harlow Lane, Dunmere, MA 01099/(508) 555-0142<br>Terms of Use/Privacy Policy</div>
  <div class="footer-apps"><span>Orchard</span><span>Botly</span><span>Zumblo</span><span>Lumavoxa</span><span>KW</span></div>
</footer>

</div>
</body>
</html>
```